Tasman Curdworks Guild needs new business cards

We need new business cards designed and produced. We are likely to need other design work done for ads, flyers etc in future.

We would like to start with an initial business card.

The Tasman Curdworks Guild (TCG) is a membership-based not-for-profit organisation that looks after the interests of Australia's small to medium artisan cheesemakers, many of whom are also small-scale farmers. The design should be simple, using our logo, but also communicate our artisan cheese and small dairy farm focus.

The first card to be designed and produced is for me, Miriam Tolhurst. My details are:

Miriam Tolhurst
Secretary
Tasman Curdworks Guild (TCG)
http://www.curdworksguild.example
T +61452837190
E miriam.miriamtolhurst@mailbox.example

I have attached the TCG logo in jpg form. I have a higher resolution version available if needed.

Thank you!

Miriam

Miriam Tolhurst
Tasman Curdworks Guild
miriam.miriamtolhurst@mailbox.example
+61452837190

Sans Serif

• Logo (see attached file)

```html
<!DOCTYPE html>
<html lang="en">
<head>
<meta charset="utf-8">
<title>Tasman Curdworks Guild – Business Card</title>
<link rel="stylesheet" href="https://fonts.googleapis.com/css2?family=EB+Garamond:ital,wght@0,400;0,600;1,400&display=swap">
<style>
  :root {
    --bg: #e6e6e6;
    --paper: #ffffff;
    --cream: #f6e7bf;
    --cream-light: #fbf1d6;
    --rind: #b9a796;
    --rind-dark: #9c8a72;
    --gold: #f8cd63;
    --gold-deep: #e8b23c;
    --brown: #5b2f14;
    --ink: #3e2a1c;
    --card-w: 540px;
    --card-h: 344px;
  }
  * { box-sizing: border-box; margin: 0; padding: 0; }
  html, body {
    width: 1200px; height: 1200px; overflow: hidden;
    background: var(--bg);
    font-family: "EB Garamond", Georgia, serif;
  }
  .sheet {
    width: 1200px; height: 1200px;
    display: flex; align-items: center; justify-content: center; gap: 40px;
  }
  .card {
    position: relative;
    width: var(--card-w); height: var(--card-h);
    overflow: hidden;
    box-shadow: 0 6px 18px rgba(0,0,0,0.18);
  }

  /* Contact side */
  .card--contact { background: var(--cream); }
  .cheese-photo {
    position: absolute; inset: 0;
    background:
      linear-gradient(160deg, var(--rind-dark) 0%, var(--rind) 22%, #d8cbb9 34%, var(--cream) 46%, var(--cream-light) 75%, var(--cream) 100%);
  }
  .edge-band { position: absolute; inset: 0; width: 100%; height: 100%; }
  .contact {
    position: absolute; right: 28px; top: 128px;
    text-align: right; color: var(--ink);
  }
  .contact__name { font-size: 29px; font-weight: 400; line-height: 1; color: var(--brown); }
  .contact__role { font-size: 19px; font-style: italic; line-height: 1.1; margin-top: 2px; }
  .contact__details { margin-top: 34px; font-size: 17.5px; line-height: 25px; }
  .contact__web { font-weight: 600; color: var(--brown); }

  /* Brand side */
  .card--brand { background: var(--paper); }
  .brand {
    position: absolute; left: 70px; top: 112px;
    display: flex; align-items: center; gap: 22px;
  }
  .brand__dot {
    width: 64px; height: 64px; border-radius: 50%;
    background: var(--gold);
    flex: none;
  }
  .brand__name {
    font-size: 31px; line-height: 38px; letter-spacing: 1.5px;
    color: var(--brown); font-weight: 400;
  }
</style>
</head>
<body>
<main class="sheet">
  <article class="card card--contact">
    <div class="cheese-photo" role="img" aria-label="Close-up photograph of a cut artisan cheese, bloomy rind above a pale creamy paste"></div>
    <svg class="edge-band" viewBox="0 0 540 344" aria-hidden="true">
      <path d="M0 0 H62 Q20 170 48 344 H0 Z" fill="var(--gold)" opacity="0.9"/>
    </svg>
    <div class="contact">
      <h1 class="contact__name">Miriam Tolhurst</h1>
      <p class="contact__role">Secretary</p>
      <p class="contact__details">
        Tasman Curdworks Guild (TCG)<br>
        <span class="contact__web">www.curdworksguild.example</span><br>
        T: +61452837190<br>
        E: miriam.miriamtolhurst@mailbox.example
      </p>
    </div>
  </article>

  <article class="card card--brand">
    <svg class="edge-band" viewBox="0 0 540 344" aria-hidden="true">
      <defs>
        <linearGradient id="band-shade" x1="0" x2="1">
          <stop offset="0" stop-color="#000" stop-opacity="0.08"/>
          <stop offset="1" stop-color="#000" stop-opacity="0"/>
        </linearGradient>
      </defs>
      <path d="M470 0 H540 V344 H512 Q455 170 470 0 Z" fill="var(--gold)"/>
      <path d="M462 0 H470 Q455 170 512 344 H500 Q445 170 462 0 Z" fill="url(#band-shade)"/>
    </svg>
    <div class="brand">
      <span class="brand__dot" aria-hidden="true"></span>
      <h2 class="brand__name">Tasman<br>Curdworks<br>Guild</h2>
    </div>
  </article>
</main>
</body>
</html>
```